Ridgewell Stonecraft Construction Needs business card

Hey we are in need of business card designs. I have upload our logo as a guideline, but free feel to run with it or come up with something unique.
Pls have fun with it and be creative. the name says it all!
i will give some directions after i see a few entries..
Logo source file has been uploaded..
Hey because of the logo is so colourful already.
Can we have a few submissions with less colour.
Also we are looking for clever/hidden/descriptive business card.

```html
<!DOCTYPE html>
<html lang="en">
<head>
<meta charset="utf-8">
<title>Ridgewell Stonecraft Construction – Business Card</title>
<link rel="stylesheet" href="https://fonts.googleapis.com/css2?family=Arimo:wght@400;700&display=swap">
<style>
  :root {
    --backdrop: #b2b2b2;
    --card: #ffffff;
    --card-edge: #5a5a5a;
    --accent-red: #ff0000;
    --brand-grey: #6e7f85;
    --tile-red: #ff2a2a;
    --tile-yellow: #ffee33;
    --tile-green: #22e622;
    --tile-cyan: #22e6f0;
    --tile-black: #222222;
  }
  * { margin: 0; padding: 0; box-sizing: border-box; }
  html, body { width: 1200px; height: 1200px; overflow: hidden; }
  body {
    background: var(--backdrop);
    font-family: "Arimo", Arial, sans-serif;
    position: relative;
  }
  .sheet-frame {
    position: absolute; inset: 2px;
    border: 2px solid #6a6a6a;
  }
  .card {
    position: absolute;
    width: 709px; height: 407px;
    background: var(--card);
    border: 2px solid var(--card-edge);
    overflow: hidden;
  }
  .card svg.tiles { position: absolute; inset: 0; width: 100%; height: 100%; }

  /* info side, tilted */
  .card--info {
    left: 155px; top: 234px;
    transform-origin: 0 0;
    transform: rotate(-12.9deg);
  }
  .info-list {
    position: absolute; left: 0; right: 0; top: 150px;
    list-style: none; text-align: center;
    color: var(--accent-red);
    font-size: 22px; line-height: 42px;
  }

  /* brand side */
  .card--brand { left: 344px; top: 693px; }
  .proprietor {
    position: absolute; left: 452px; top: 24px;
    color: var(--accent-red);
    font-size: 17px; letter-spacing: 2px;
    font-variant: small-caps; line-height: 24px;
  }
  .brand {
    position: absolute; left: 0; width: 709px; top: 84px;
    text-align: center;
  }
  .brand-mark {
    display: block; width: 40px; height: 40px; margin: 0 auto 14px;
    background: var(--brand-grey);
  }
  .brand-name {
    color: var(--brand-grey);
    font-size: 27px; font-weight: 400; letter-spacing: -0.3px;
  }
  .contact-line {
    position: absolute; left: 0; width: 709px; top: 230px;
    text-align: center;
    color: var(--accent-red);
    font-size: 18px; font-weight: 700; letter-spacing: 2px;
    font-variant: small-caps;
  }
</style>
</head>
<body>
  <div class="sheet-frame"></div>

  <section class="card card--info">
    <svg class="tiles" viewBox="0 0 709 407" role="img" aria-label="Border of coloured building-block tiles in red, yellow, green, cyan and black">
      <defs>
        <linearGradient id="tileBlendInfo" x1="0" y1="0" x2="1" y2="1">
          <stop offset="0" stop-color="var(--tile-red)"/>
          <stop offset="0.3" stop-color="var(--tile-yellow)"/>
          <stop offset="0.6" stop-color="var(--tile-green)"/>
          <stop offset="1" stop-color="var(--tile-cyan)"/>
        </linearGradient>
      </defs>
      <path fill="url(#tileBlendInfo)" fill-opacity="0.55" fill-rule="evenodd"
            d="M0 0H709V407H0Z M120 85H600V322H120Z"/>
    </svg>
    <ul class="info-list">
      <li>Work Features</li>
      <li>Work specialty</li>
      <li>Contact Details</li>
    </ul>
  </section>

  <section class="card card--brand">
    <svg class="tiles" viewBox="0 0 709 407" role="img" aria-label="Stepped arrangement of coloured building-block tiles along the lower edge">
      <defs>
        <linearGradient id="tileBlendBrand" x1="0" y1="0" x2="1" y2="0">
          <stop offset="0" stop-color="var(--tile-red)"/>
          <stop offset="0.35" stop-color="var(--tile-yellow)"/>
          <stop offset="0.65" stop-color="var(--tile-green)"/>
          <stop offset="1" stop-color="var(--tile-cyan)"/>
        </linearGradient>
      </defs>
      <path fill="url(#tileBlendBrand)" fill-opacity="0.55"
            d="M0 120H38V192H107V323H217V364H392V323H565V263H602V162H709V407H0Z"/>
    </svg>
    <div class="proprietor">
      <div>Proprietor Name</div>
      <div>000000000</div>
    </div>
    <div class="brand">
      <span class="brand-mark"></span>
      <div class="brand-name">Ridgewell Stonecraft Construction</div>
    </div>
    <div class="contact-line">Email, Address</div>
  </section>
</body>
</html>
```